Silver Kettle Consulting

I need a business card design and for my consulting business. I provide outsourced CFO services for start-ups and high growth companies. I call my company Silver Kettle because building a company is similar to building a stone pathway, selecting each stone and planning several stones head in order to properly place them - all while keeping an eye on the final design and curve of the path. The underlying idea I want to express with my marketing images is that I'm someone that you can count on to help build your business and be there step by step to help. I'm not the old gray-haired CFO that many folks think of. :) I've included a one-page summery that I'm working on, it includes a summary of what I do. I've used a muted pathway and with greens in the header , and do like the green, but am open to other colors if they work well. Would like something that looks like a pathway, but a more abstract version instead of a picture.

Marketing

```html
<!DOCTYPE html>
<html lang="en">
<head>
<meta charset="UTF-8">
<title>Silver Kettle Consulting – Business Card</title>
<link href="https://fonts.googleapis.com/css2?family=Source+Sans+3:wght@400;600;700&display=swap" rel="stylesheet">
<style>
  :root {
    --green: #2f6f35;
    --card: #f7f7f6;
    --ink: #333333;
    --backdrop: #d9d9d9;
  }
  * { margin: 0; padding: 0; box-sizing: border-box; }
  html, body {
    width: 1200px; height: 900px; overflow: hidden;
    background: var(--backdrop);
    font-family: "Source Sans 3", "Source Sans Pro", sans-serif;
  }
  .canvas { position: relative; width: 1200px; height: 900px; }
  .card {
    position: absolute; left: 250px; width: 700px; height: 400px;
    background: var(--card);
    overflow: hidden;
    box-shadow: 0 6px 18px rgba(0,0,0,0.18);
  }
  .card--back { top: 35px; }
  .card--front { top: 465px; }

  .rule { position: absolute; height: 4px; background: var(--green); }

  /* Back side */
  .card--back .rule { left: 0; right: 290px; top: 158px; }
  .brand-pill {
    position: absolute; right: 0; top: 128px; width: 300px; height: 84px;
    background: var(--green);
    border-radius: 42px 0 0 42px;
    display: flex; align-items: center; padding-left: 32px;
  }
  .brand-pill__name {
    color: #fff; font-weight: 700; font-size: 32px; letter-spacing: 0.5px;
    white-space: nowrap;
  }
  .tagline {
    position: absolute; right: 16px; top: 222px;
    color: var(--green); font-weight: 700; font-size: 15px;
    white-space: nowrap;
  }
  .socials { position: absolute; left: 40px; top: 250px; list-style: none; }
  .socials li {
    display: flex; align-items: center; gap: 12px;
    color: var(--ink); font-weight: 600; font-size: 17px;
    margin-bottom: 14px;
  }
  .socials__mark { width: 20px; height: 20px; background: var(--green); border-radius: 3px; }

  /* Front side */
  .logo-text {
    position: absolute; left: 32px; top: 28px;
    color: var(--green); font-weight: 700; font-size: 40px; letter-spacing: 0.5px;
    white-space: nowrap;
  }
  .name-pill {
    position: absolute; left: 0; top: 92px; width: 375px; height: 92px;
    background: var(--green);
    border-radius: 0 46px 46px 0;
    padding: 10px 0 0 34px;
    color: #fff;
  }
  .name-pill__name { font-weight: 700; font-size: 36px; line-height: 1.1; white-space: nowrap; }
  .name-pill__role {
    font-weight: 600; font-size: 16px; letter-spacing: 0.5px;
    text-transform: uppercase; margin: 4px 0 0 64px;
  }
  .card--front .rule { left: 382px; right: 0; top: 140px; }

  .contact { position: absolute; left: 30px; top: 240px; list-style: none; }
  .contact li {
    display: flex; align-items: center; gap: 18px;
    color: var(--ink); font-weight: 600; font-size: 17px; letter-spacing: 0.5px;
    margin-bottom: 14px; white-space: nowrap;
  }
  .contact svg, .address svg { width: 16px; height: 16px; flex: none; }
  .address {
    position: absolute; left: 430px; top: 300px;
    display: flex; gap: 14px; align-items: flex-start;
    color: var(--ink); font-weight: 600; font-size: 17px; letter-spacing: 0.5px;
    line-height: 1.3; text-transform: uppercase;
  }
  .address svg { margin-top: 2px; }
</style>
</head>
<body>
<main class="canvas">

  <section class="card card--back" aria-label="Card back">
    <div class="rule"></div>
    <div class="brand-pill"><span class="brand-pill__name">SILVER KETTLE</span></div>
    <p class="tagline">Steady Finance Guidance For Every Growth Stage</p>
    <ul class="socials">
      <li><span class="socials__mark"></span>SILVERKETTLE</li>
      <li><span class="socials__mark"></span>@SILVERKETTLE</li>
    </ul>
  </section>

  <section class="card card--front" aria-label="Card front">
    <p class="logo-text">SILVER KETTLE</p>
    <div class="name-pill">
      <p class="name-pill__name">Dana Whitlock</p>
      <p class="name-pill__role">General Manager</p>
    </div>
    <div class="rule"></div>

    <ul class="contact">
      <li>
        <svg viewBox="0 0 16 16" aria-hidden="true"><path d="M4 1.5 6 4.5 4.8 6c.8 1.9 2.3 3.4 4.2 4.2L10.5 9l3 2-1.2 2.6C7 13.6 2.4 9 2.4 3.7Z" fill="var(--green)"/></svg>
        555-014-2238
      </li>
      <li>
        <svg viewBox="0 0 16 16" aria-hidden="true"><rect x="1.5" y="3.5" width="13" height="9" fill="none" stroke="var(--green)" stroke-width="1.5"/><path d="M1.5 3.5 8 9l6.5-5.5" fill="none" stroke="var(--green)" stroke-width="1.5"/></svg>
        DANA@SILVERKETTLECO.COM
      </li>
      <li>
        <svg viewBox="0 0 16 16" aria-hidden="true"><circle cx="8" cy="8" r="6.5" fill="none" stroke="var(--green)" stroke-width="1.5"/><ellipse cx="8" cy="8" rx="2.8" ry="6.5" fill="none" stroke="var(--green)" stroke-width="1.2"/><path d="M1.5 8h13" stroke="var(--green)" stroke-width="1.2"/></svg>
        WWW.SILVERKETTLECO.COM
      </li>
    </ul>

    <div class="address">
      <svg viewBox="0 0 16 16" aria-hidden="true"><path d="M8 1.5 1 8h2v6.5h4v-4h2v4h4V8h2Z" fill="var(--green)"/></svg>
      <p>418 Alder Grove Rd,<br>Portland, USA</p>
    </div>
  </section>

</main>
</body>
</html>
```